Church Lanterns Over Millbrook Gospel Booklet Design

We need a booklet designed that we will be printing to hand out in our community. Wording for each page will be provided and we need graphic design to produce the layouts in a format ready for print. Booklet will be 4.75" x 4.75" square and a total of 12 pages: 1 cover page front, 1 cover page back, 10 inside pages some of which will be full spread across 2 pages.

Target Market(s)

English speaking Westerners

Industry/Entity Type

Religious

Font styles to use
Serif

Colors
ffffff
85abd2
0292cd
33b8a4
5c5c5c

Requirements
Must have
• Minimalist design with clean look described in attached document
Nice to have
• Aesthetically pleasing graphics, crisp fonts, excellent turn around times
Should not have
• Effeminate design, busy look with too much graphic and text

```html
<!DOCTYPE html>
<html lang="en">
<head>
<meta charset="utf-8">
<title>Lanterns Over Millbrook – Gospel Booklet Layouts</title>
<link href="https://fonts.googleapis.com/css2?family=Cinzel:wght@400;500&family=EB+Garamond:wght@400;500&family=Arvo&family=Fira+Sans:wght@600&display=swap" rel="stylesheet">
<style>
  :root{
    --bg:#dcf5f2;
    --paper:#f6f7f7;
    --white:#ffffff;
    --sky:#85abd2;
    --blue:#0292cd;
    --teal:#33b8a4;
    --ink:#5c5c5c;
    --ink-dark:#3a3a3a;
    --band:linear-gradient(90deg,var(--teal),var(--blue));
    --band-rev:linear-gradient(90deg,var(--blue),var(--teal));
  }
  *{box-sizing:border-box;margin:0;padding:0}
  html,body{width:1200px;height:1200px;overflow:hidden;background:var(--bg)}
  .stage{position:relative;width:1200px;height:1200px}
  .item{position:absolute}
  .spread{display:flex}
  .page{position:relative;background:var(--paper);overflow:hidden;color:var(--ink);font-family:"EB Garamond",Georgia,serif}
  .label{position:absolute;font-family:"Fira Sans",Arial,sans-serif;font-weight:600;font-size:20px;color:#111;letter-spacing:.3px;transform:translateX(-50%);white-space:nowrap}

  /* covers */
  .wash{position:absolute;left:0;top:0;width:100%;height:62%;
    background:radial-gradient(ellipse at 30% 20%,rgba(133,171,210,.55),transparent 60%),
               radial-gradient(ellipse at 80% 10%,rgba(133,171,210,.45),transparent 55%),
               linear-gradient(180deg,#b9d3e0 0%,#dbe8ee 45%,var(--paper) 100%)}
  .cover-title{position:absolute;right:14px;top:216px;display:flex;align-items:baseline;gap:5px;color:var(--ink-dark);white-space:nowrap}
  .cover-title .lead{font-family:"EB Garamond",Georgia,serif;font-size:14px}
  .cover-title .main{font-family:"Cinzel",Georgia,serif;font-size:25px;letter-spacing:.2px}
  .cover-rule{position:absolute;left:0;top:246px;width:130px;height:3px;background:var(--band)}

  .contact{position:absolute;left:0;width:100%;top:214px;text-align:center;font-size:6.4px;line-height:9px;color:var(--ink-dark)}
  .contact .org{text-transform:uppercase;letter-spacing:.3px}
  .back-rule{position:absolute;left:0;top:243px;width:100%;height:3px;background:var(--band)}
  .credits{position:absolute;left:0;width:100%;top:251px;text-align:center;font-family:Arial,sans-serif;font-size:4.4px;line-height:6px;color:var(--ink)}

  /* inner pages */
  .top-line{position:absolute;left:0;top:0;width:100%;height:3px;background:var(--band)}
  .bottom-band{position:absolute;left:0;bottom:0;width:100%;height:28px;background:var(--band)}
  .bottom-band.rev{background:var(--band-rev)}
  .wing-mark{position:absolute;left:50%;width:13px;height:9px;margin-left:-6px;border-radius:50% 50% 40% 40%;background:#9aa3a5}
  .copy{position:absolute;left:22px;right:22px;text-align:center;font-size:9.6px;line-height:13px}
  .copy p+p{margin-top:10px}
  .copy.left{text-align:left}
  .copy ol{margin-top:10px;padding-left:10px}
  .copy li{margin-bottom:5px;padding-left:2px}

  .photo{position:absolute;inset:0}
  .photo-cross{background:radial-gradient(ellipse at 62% 45%,#e8a77a 0%,#b77a5c 18%,#6d6258 40%,#343b39 70%,#1f2624 100%)}
  .photo-sky{background:linear-gradient(180deg,#3f6f8e 0%,#6f95ad 30%,#a7b5bd 52%,#c29583 66%,#4f5966 82%,#2f3744 100%)}
  .photo-credit{position:absolute;left:12px;bottom:7px;font-family:Arial,sans-serif;font-size:4.4px;color:rgba(255,255,255,.75)}

  .verse{position:absolute;left:0;width:100%;top:84px;text-align:center;color:var(--white);font-family:"Arvo",Georgia,serif;text-transform:uppercase}
  .verse .sm{font-size:9.4px;letter-spacing:1.3px;line-height:19px}
  .verse .lg{font-size:17px;letter-spacing:1.6px;line-height:26px}
  .verse .ref{margin-top:52px;font-size:10px;letter-spacing:1.4px}
</style>
</head>
<body>
<main class="stage">

  <!-- Front cover -->
  <section class="item" style="left:132px;top:64px">
    <div class="page" style="width:274px;height:274px">
      <div class="wash" role="img" aria-label="Soft blue watercolour sky wash"></div>
      <h1 class="cover-title"><span class="lead">Lanterns Over</span><span class="main">MILLBROOK</span></h1>
      <div class="cover-rule"></div>
    </div>
  </section>
  <div class="label" style="left:270px;top:356px">FRONT COVER</div>

  <!-- Front & back cover -->
  <section class="item spread" style="left:570px;top:64px">
    <div class="page" style="width:264px;height:274px">
      <div class="wash" role="img" aria-label="Soft blue watercolour sky wash"></div>
      <div class="contact"><div class="org">Lanterns Over Millbrook</div><div>24 Alder Creek Road Millbrook, CA 90218</div><div>P: +01 555 0142 &nbsp;E: hello@lanternsmillbrook.org</div></div>
      <div class="back-rule"></div>
      <div class="credits"><div>© Images and vector graphics by Harbor Studio. Photo by R. Lind on Open Frame.</div><div>Icons designed by Harbor Studio from harborstudio.co</div></div>
    </div>
    <div class="page" style="width:264px;height:274px">
      <div class="wash" role="img" aria-label="Soft blue watercolour sky wash"></div>
      <div class="cover-title" style="right:8px"><span class="lead">Lanterns Over</span><span class="main" style="font-size:24px">MILLBROOK</span></div>
      <div class="cover-rule" style="width:124px"></div>
    </div>
  </section>
  <div class="label" style="left:832px;top:356px">FRONT &amp; BACK COVER</div>

  <!-- Back cover -->
  <section class="item" style="left:134px;top:446px">
    <div class="page" style="width:274px;height:276px">
      <div class="wash" role="img" aria-label="Soft blue watercolour sky wash"></div>
      <div class="contact" style="top:216px"><div class="org">Lanterns Over Millbrook</div><div>24 Alder Creek Road Millbrook, CA 90218</div><div>P: +01 555 0142 &nbsp;E: hello@lanternsmillbrook.org</div></div>
      <div class="back-rule" style="top:245px"></div>
      <div class="credits" style="top:253px"><div>© Images and vector graphics by Harbor Studio. Photo by R. Lind on Open Frame.</div><div>Icons designed by Harbor Studio from harborstudio.co</div></div>
    </div>
  </section>
  <div class="label" style="left:270px;top:742px">BACK COVER</div>

  <!-- Page 2 - 3 -->
  <section class="item spread" style="left:567px;top:446px">
    <div class="page" style="width:265px;height:278px">
      <div class="photo photo-cross" role="img" aria-label="Photo of a wooden cross on a hill at sunrise with a faint dove outline"></div>
      <div class="photo-credit">© Image and vector graphic by Harbor Studio</div>
    </div>
    <div class="page" style="width:268px;height:278px">
      <div class="top-line"></div>
      <div class="wing-mark" style="top:72px" role="img" aria-label="Small wing ornament"></div>
      <div class="copy" style="top:100px"><p>God willingly created the universe, meaning he envisioned, designed, and made us.</p><p>“In the beginning God created the heavens and the earth.”<br>(Genesis 1:1)</p></div>
      <div class="bottom-band"></div>
    </div>
  </section>
  <div class="label" style="left:826px;top:742px">PAGE 2 - 3</div>

  <!-- Page 4 - 5 -->
  <section class="item spread" style="left:44px;top:838px">
    <div class="page" style="width:265px;height:280px">
      <div class="top-line"></div>
      <div class="wing-mark" style="top:24px" role="img" aria-label="Small wing ornament"></div>
      <div class="copy left" style="top:52px;font-size:9.2px;line-height:12.6px"><p>This reality establishes some foundational truths for all of us:</p>
        <ol><li>God loves us - he didn’t have to create us; we are here because he couldn’t imagine life without us.</li><li>God is the proper authority in our lives - if he designed and made us, he rightfully owns us.</li><li>God knows the purpose of our lives - if he designed and made us, he knows why we are here.</li><li>God’s truth is the truth we need - if he designed and made us, he knows what it takes for life to go well for us.</li></ol></div>
      <div class="bottom-band"></div>
    </div>
    <div class="page" style="width:269px;height:280px">
      <div class="top-line"></div>
      <div class="wing-mark" style="top:60px" role="img" aria-label="Small wing ornament"></div>
      <div class="copy" style="top:88px"><p>But we, mankind, have all rejected God’s authority in our lives. And because he rightfully owns us, our rebellion against God is a grave injustice; an act of treason for which we deserve to be cut off from God forever.</p><p>“For the wages of sin is death...”<br>(Romans 6:23)</p></div>
      <div class="bottom-band rev"></div>
    </div>
  </section>
  <div class="label" style="left:312px;top:1134px">PAGE 4 - 5</div>

  <!-- Page 10 - 11 -->
  <section class="item spread" style="left:623px;top:838px">
    <div class="page" style="width:264px;height:276px">
      <div class="top-line"></div>
      <div class="wing-mark" style="top:66px" role="img" aria-label="Small wing ornament"></div>
      <div class="copy" style="top:94px;left:26px;right:26px;font-size:9.2px;line-height:12.8px"><p>Next, God has given us the Bible and his church as the key tools for us to grow in our understanding of God and our personal relationship with him. So, it is essential you find a local church that believes the Bible is 100% true. Tell one of the pastors you are a brand new Christian and they will help you from there.</p></div>
      <div class="bottom-band"></div>
    </div>
    <div class="page" style="width:268px;height:276px">
      <div class="photo photo-sky" role="img" aria-label="Photo of a sky above clouds at dusk"></div>
      <div class="verse"><div class="sm">If you confess with your mouth,</div><div class="lg">“Jesus is Lord,”</div><div class="sm">and believe in your heart that</div><div class="sm">God raised him from the dead,</div><div class="lg">You will be saved.</div><div class="ref">Romans 10:9</div></div>
      <div class="photo-credit" style="left:10px;bottom:5px">Photo by R. Lind on Open Frame</div>
    </div>
  </section>
  <div class="label" style="left:890px;top:1134px">PAGE 10 - 11</div>

</main>
</body>
</html>
```